Ich biete Employer-Branding-Beratung für mittelständische Unternehmen, d.h. ich entwickle für und mit meinen Kunden ihre Arbeitgebermarke und Arbeitgeberkommunikation, um leichter neue Mitarbeitende zu finden.
Meine Zielgruppe: mittelständische Unternehmen (1.000-4.000 Mitarbeitende), dort v.a. die Personalabteilung, meist Frauen
- Klappkarte im Format DIN lang. Die Karte soll sich dafür eignen, sie auf den Schreibtisch zu stellen.
- Corporate Design siehe Anhang. Darin ist bereits ein Entwurf für eine Karte enthalten. Der darf gern genau so übernommen werden. Ich freue mich aber auch über gute neue Entwürfe, die das CD aufgreifen.
- Seite 1: Logo & Zitat & Autor: 'Wege entstehen dadurch, dass man sie geht.' // Otto Rembel
- Seite 2: Text: Auf ein Jahr 2024 mit neuen Wegen!
- Seite 3: leer
- Seite 4: Adresse/Kontaktdaten:
Friederike Storm
Die Teamkultur-Expertin
Lindenweg 42
04109 Leipzig
T +49 (15 23) 917 20 48
E fs@die-teamkultur-expertin.de
Hinweis: Die Karte wird in durchsichtigen Umschlägen verschickt, die Adresse sollte so kontrastreich sein, dass man sie auch durch den Umschläge sehen kann, falls Briefe zurück kommen.

```html
<!DOCTYPE html>
<html lang="de">
<head>
<meta charset="utf-8">
<title>Klappkarte 2024 – Die Teamkultur-Expertin</title>
<link rel="stylesheet" href="https://fonts.googleapis.com/css2?family=Barlow:wght@300;400;500;600&display=swap">
<style>
  :root {
    --plum: #560f32;
    --plum-soft: #c3a9b5;
    --plum-line: #b48a9d;
    --navy: #0e3a5c;
    --navy-soft: #b2b5c6;
    --navy-line: #8fa0b4;
    --ink: #163a5e;
    --paper: #ffffff;
  }
  * { box-sizing: border-box; margin: 0; padding: 0; }
  html, body {
    width: 1200px; height: 849px; overflow: hidden;
    background: var(--paper);
    font-family: "Barlow", "DIN Alternate", Arial, sans-serif;
  }
  .canvas { position: relative; width: 1200px; height: 849px; }

  .side-label {
    position: absolute; font-size: 11.5px; font-weight: 400;
    color: var(--ink); letter-spacing: 0.03em;
  }
  .side-label--outside { left: 102px; top: 559px; }
  .side-label--inside { left: 663px; top: 259px; }

  .card {
    position: absolute; width: 489px; height: 489px;
    background: var(--paper);
  }
  .card--outside { left: 89.5px; top: 59px; border: 0.6px solid var(--plum-line); }
  .card--inside { left: 641.5px; top: 302px; border: 0.6px solid var(--navy-line); }
  .card__shapes { position: absolute; inset: 0; width: 100%; height: 100%; }

  .headline {
    position: absolute; color: var(--paper);
    font-weight: 300; font-size: 28px; line-height: 33px;
    letter-spacing: 0.01em; text-transform: uppercase;
  }
  .card--outside .headline { left: 263px; top: 54px; }
  .card--inside .headline { left: 24px; top: 59px; }

  .quote-author {
    position: absolute; left: 384px; top: 223px;
    color: var(--paper); font-size: 9px; font-weight: 400; letter-spacing: 0.03em;
  }

  .contact {
    position: absolute; left: 18px; top: 382px;
    color: var(--ink); font-size: 8.4px; line-height: 11.6px;
    font-weight: 500; letter-spacing: 0.02em; font-style: normal;
  }
  .contact__name { font-weight: 600; }
  .contact__gap { height: 11.6px; }

  .brand-name {
    position: absolute; right: 16px; bottom: 28px;
    color: var(--ink); font-size: 11px; font-weight: 500;
    letter-spacing: 0.12em; text-transform: uppercase;
  }
</style>
</head>
<body>
<main class="canvas">

  <section class="card card--outside" aria-label="Außenseite">
    <svg class="card__shapes" viewBox="0 0 930 930" preserveAspectRatio="none" aria-hidden="true">
      <polygon points="0,0 930,0 930,595 0,419" fill="var(--plum)"/>
      <polygon points="0,419 725,556 0,695" fill="var(--plum-soft)"/>
      <line x1="464" y1="-2" x2="464" y2="934" stroke="var(--plum-line)" stroke-width="1.2"/>
    </svg>

    <address class="contact">
      <div class="contact__name">Friederike Storm</div>
      <div>Die Teamkultur-Expertin</div>
      <div>Lindenweg 42</div>
      <div>04109 Leipzig</div>
      <div class="contact__gap"></div>
      <div>T: +49 (15 23) 917 20 48</div>
      <div>E: fs@die-teamkultur-expertin.de</div>
      <div>www.die-teamkultur-expertin.de</div>
    </address>

    <h1 class="headline">Wege<br>entstehen<br>dadurch,<br>dass man<br>sie geht.</h1>
    <p class="quote-author">Otto Rembel</p>

    <p class="brand-name">Die Teamkultur-Expertin</p>
  </section>
  <p class="side-label side-label--outside">Außen</p>

  <p class="side-label side-label--inside">Innen</p>
  <section class="card card--inside" aria-label="Innenseite">
    <svg class="card__shapes" viewBox="0 0 930 930" preserveAspectRatio="none" aria-hidden="true">
      <polygon points="0,0 465,0 465,507 0,595" fill="var(--navy)"/>
      <polygon points="0,595 465,507 465,730 0,643" fill="var(--navy-soft)"/>
      <line x1="465" y1="-6" x2="465" y2="934" stroke="var(--navy-line)" stroke-width="1.2"/>
    </svg>
    <h2 class="headline">Auf ein<br>Jahr 2024<br>mit neuen<br>Wegen!</h2>
  </section>

</main>
</body>
</html>
```